Q7M Electrical Systems Inc Business Cards

Target Market(s)

Customers

Industry/Entity Type

Construction - Electrical

Contact Information for Business Card

Company Name, Address, Phone, and email address

Font styles to use
Sans Serif

Colors
0054AA
0677BA
7BADD7
CADEEF
E8F1F8

Requirements
Must have
• we would like to use the same design that we had our vehicles wrapped
Nice to have
• The design that we used on our trucks

```html
<!DOCTYPE html>
<html lang="en">
<head>
<meta charset="utf-8">
<title>Q7M Electrical Systems Inc Business Cards</title>
<link href="https://fonts.googleapis.com/css2?family=Poppins:wght@400;600&display=swap" rel="stylesheet">
<style>
  :root {
    --navy: #0b1336;
    --white: #ffffff;
    --stage: #e6e3de;
    --ink: #1a1a1a;
  }
  * { margin: 0; padding: 0; box-sizing: border-box; }
  html, body {
    width: 1189px; height: 1200px; overflow: hidden;
    background: var(--stage);
    font-family: 'Poppins', sans-serif;
  }
  .card {
    position: absolute; left: 169px; width: 851px; height: 484px;
    border-radius: 32px;
    box-shadow: 0 6px 18px rgba(0,0,0,0.18);
  }
  .card--front { top: 112px; background: var(--navy); }
  .card--back { top: 641px; background: var(--white); }

  .brand {
    position: absolute; text-align: center; font-weight: 600; line-height: 1;
  }
  .brand__name { display: block; }
  .brand__sub { display: block; letter-spacing: 0.32em; }

  .card--front .brand {
    left: 0; right: 0; top: 150px; color: var(--white);
  }
  .card--front .brand__name { font-size: 118px; letter-spacing: -0.01em; }
  .card--front .brand__sub { font-size: 22px; margin-top: 26px; }

  .card--back .brand {
    left: 85px; width: 280px; top: 180px; color: var(--navy);
  }
  .card--back .brand__name { font-size: 78px; }
  .card--back .brand__sub { font-size: 14px; margin-top: 18px; letter-spacing: 0.22em; }

  .divider {
    position: absolute; left: 425px; top: 159px; width: 2px; height: 178px;
    background: var(--navy);
  }
  .contact {
    position: absolute; left: 478px; width: 300px; top: 168px;
    text-align: center; color: var(--ink); font-size: 21px; font-weight: 400;
  }
  .contact__line { display: block; line-height: 27px; white-space: nowrap; }
  .contact__rule {
    width: 221px; height: 2px; background: var(--ink); margin: 10px auto 9px;
  }
  .contact__icons { display: flex; justify-content: center; gap: 9px; margin-bottom: 6px; }
  .contact__icons svg { width: 23px; height: 23px; }
</style>
</head>
<body>
  <section class="card card--front">
    <div class="brand">
      <span class="brand__name">Q7M</span>
      <span class="brand__sub">ELECTRICAL SYSTEMS INC.</span>
    </div>
  </section>

  <section class="card card--back">
    <div class="brand">
      <span class="brand__name">Q7M</span>
      <span class="brand__sub">ELECTRICAL SYSTEMS INC.</span>
    </div>
    <div class="divider"></div>
    <div class="contact">
      <span class="contact__line">418 Harbor Point Way # 210</span>
      <span class="contact__line">Lakemont Springs, FL 32790</span>
      <div class="contact__rule"></div>
      <div class="contact__icons">
        <svg viewBox="0 0 24 24" aria-label="Phone">
          <circle cx="12" cy="12" r="12" fill="var(--navy)"/>
          <path d="M9 6.5c.5 0 1 1.8 1.3 2.6.2.6-.8 1.2-.8 1.6.3 1.5 1.8 3 3.2 3.4.4 0 1-1 1.6-.8.8.3 2.5 1 2.5 1.5 0 1-1 2.2-2.2 2.2C10 17 7 13.8 7 8.6 7 7.5 8 6.5 9 6.5z" fill="var(--white)"/>
        </svg>
        <svg viewBox="0 0 24 24" aria-label="Email">
          <circle cx="12" cy="12" r="12" fill="var(--navy)"/>
          <rect x="6.5" y="8" width="11" height="8" rx="1" fill="none" stroke="var(--white)" stroke-width="1.5"/>
          <path d="M6.8 8.5 12 12.5l5.2-4" fill="none" stroke="var(--white)" stroke-width="1.5"/>
        </svg>
      </div>
      <span class="contact__line">407-555-0142</span>
      <span class="contact__line">info@q7melectric.com</span>
    </div>
  </section>
</body>
</html>
```